3D abstract logo Construction, Kitchen and Bath design and Project Management Business Card Design

I want a 3d abstract logo for a new General Construction, Kitchen and Bath design and Project Management Company located at Philadelphia PA, we want to put our logo in the white color trucks too. I want to look professional and serious at the same time look like an architect design and the warm originals color that make you feel in a nice decorated home, I like the colors trend in this link:
http://www.quillorbit.example/qo/kts/cardmaker.aspx?alt_doc_id=RM41T-K7B93-2W5&doc_id=5130948826&pf_id=H4D

I was thinking about a roof and the PA font could have square shape or like wood framing with two tones of the brick color black and creamy yellow color.... Also I like the keystone Idea like the modification or the LK Skyroute logo but curvy at the top

The final design should communicate big company (because we want to grow), responsible, professional and organized that really care about our customers and give them everything they need... plan and design, excellent labor and Project Management
Updates

I doesn't have to be 3d

Reason: I haven't received enough options...

Please stick with the warm tones shown in the image001 attached I like spicy cinnamon instead a cold wine or brick color and also the cream yellowish tones added

Hello designers, please use only the idea and colors of the image001 I don't want to be stick with a house logo because I do commercial construction too so I prefer work around the keystone idea maybe leaving the style of the PA.
I'd like the base tone on the card dark like first option and you can send me a white option too.

Please send me your ideas as soon as possible 

Thank you so much!

Target Market(s)

Builders, State, commercial business owners, Property owners or Real State and Property Management Companies

Industry/Entity Type

Architect

Contact Information for Business Card

LK Buildworks LLC
“Your project is our business”
Renata Solvik Eng.
President
Commercial & Residential General Construction
Kitchen & Bath Design | Project Management
Phone: 215-738-4196 | Fax: 215-738-4197 Cell: 856-390-7712
renata@lkbuildworks.example

```html
<!DOCTYPE html>
<html lang="en">
<head>
<meta charset="utf-8">
<title>LK Buildworks – Business Card</title>
<link href="https://fonts.googleapis.com/css2?family=Arimo:ital,wght@0,400;0,700;1,400&family=Noto+Sans:wght@400&display=swap" rel="stylesheet">
<style>
  :root {
    --cinnamon: #a50012;
    --cinnamon-deep: #8e000f;
    --rose: #d0344a;
    --cream: #fdfbe6;
    --ink: #111111;
    --paper: #ffffff;
  }
  * { margin: 0; padding: 0; box-sizing: border-box; }
  html, body { width: 741px; height: 1200px; overflow: hidden; background: var(--paper); }
  body { position: relative; font-family: "Arimo", Arial, sans-serif; }

  .card-front {
    position: absolute; left: 0; top: 0; width: 741px; height: 435px;
    background: var(--cream); overflow: hidden;
  }
  .accent-panel {
    position: absolute; left: 672px; top: 0; width: 69px; height: 435px;
    background: linear-gradient(180deg, var(--cinnamon) 0%, var(--cinnamon-deep) 100%);
  }

  .person-name {
    position: absolute; left: 37px; top: 36px;
    font-weight: 700; font-size: 41px; letter-spacing: 1.6px;
    color: var(--cinnamon); line-height: 1;
  }
  .person-title {
    position: absolute; left: 39px; top: 85px;
    font-style: italic; font-size: 24px; color: var(--cinnamon); line-height: 1;
  }
  .services {
    position: absolute; left: 37px; top: 142px;
    font-family: "Noto Sans", Verdana, sans-serif;
    font-size: 24px; letter-spacing: 1.1px; line-height: 28px; color: var(--rose);
  }

  .contact-list { position: absolute; left: 37px; top: 287px; list-style: none; }
  .contact-list li { display: flex; height: 32.5px; align-items: baseline; }
  .contact-label { width: 102px; font-size: 19px; color: var(--cinnamon); }
  .contact-list li:last-child .contact-label { font-size: 21px; }
  .contact-value { font-size: 18px; color: var(--ink); }

  .front-brand {
    position: absolute; left: 486px; top: 300px; width: 176px;
    text-align: center; font-weight: 700; font-size: 22px; line-height: 26px;
    color: var(--cinnamon); letter-spacing: 0.5px;
  }

  .card-back {
    position: absolute; left: 137px; top: 458px; width: 434px; height: 742px;
    background: var(--cream); text-align: center;
  }
  .back-brand {
    position: absolute; left: 0; right: 0; top: 330px;
    font-weight: 700; font-size: 40px; line-height: 46px;
    color: var(--cinnamon); letter-spacing: 1px;
  }
  .slogan {
    position: absolute; left: 0; right: 0; top: 484px;
    font-size: 24px; color: var(--cinnamon);
  }
  .website {
    position: absolute; left: 0; right: 0; top: 635px;
    font-size: 19px; color: var(--rose);
  }
</style>
</head>
<body>
  <section class="card-front">
    <div class="accent-panel" role="img" aria-label="Decorative warm cinnamon accent band"></div>

    <h1 class="person-name">RENATA SOLVIK</h1>
    <p class="person-title">Eng. President</p>
    <p class="services">Commercial &amp; Residential General<br>Construction Kitchen &amp; Bath Design</p>

    <ul class="contact-list">
      <li><span class="contact-label">Phone:</span><span class="contact-value">215-738-4196</span></li>
      <li><span class="contact-label">Fax:</span><span class="contact-value">215-738-4197</span></li>
      <li><span class="contact-label">Cell:</span><span class="contact-value">856-390-7712</span></li>
      <li><span class="contact-label">Email:</span><span class="contact-value">renata@lkbuildworks.example</span></li>
    </ul>

    <p class="front-brand">LK<br>BUILDWORKS</p>
  </section>

  <section class="card-back">
    <p class="back-brand">LK<br>BUILDWORKS</p>
    <p class="slogan">Your project is our business</p>
    <p class="website">www.lkbuildworks.example</p>
  </section>
</body>
</html>
```